BSC Flyer to attract applicants 11x17

Brightline Stagecraft Company provides crew for local concerts, filming, theater, and corporate events.
The flyer will be posted on bulletin boards at colleges with theater programs.
Our primary venues are historic theaters in downtown LA
Need a 11x17 poster to attract potential applicants/crew
I have attached a poster that one of our staff made that has all if the relevant info - but i know the poster can look much better than that. I have also attached many images and our logo. It is not necessary to use all of the images, or any of them. The two images of the theater interiors are the venues we operate so they would be the first to include. I can send additional info or images upon request. Thank you

Entertainment

• APPLY@BSCCREWHUB.LA

```html
<!DOCTYPE html>
<html lang="en">
<head>
<meta charset="utf-8">
<title>Brightline Stagecraft Company – We're Hiring Technicians</title>
<link rel="stylesheet" href="https://fonts.googleapis.com/css2?family=Montserrat:wght@300;500;700;800&family=Poppins:wght@800;900&display=swap">
<style>
  :root {
    --backdrop: #d4d6d5;
    --royal: #0a3fc2;
    --royal-deep: #0630a0;
    --navy: #07145a;
    --ink: #0b1236;
    --white: #ffffff;
    --tab-grey: #eef0f3;
  }
  html, body {
    margin: 0;
    width: 1200px;
    height: 900px;
    overflow: hidden;
    background: var(--backdrop);
    font-family: "Montserrat", sans-serif;
  }
  .poster {
    position: absolute;
    left: 322px;
    top: 20px;
    width: 556px;
    height: 860px;
    overflow: hidden;
    background: var(--royal);
    box-shadow: 0 10px 30px rgba(0,0,0,0.18);
  }
  .theater-photo {
    position: absolute;
    left: 0; top: 0;
    width: 100%;
    height: 470px;
    background:
      radial-gradient(ellipse 38% 30% at 50% 48%, rgba(150,140,210,0.55) 0%, transparent 100%),
      radial-gradient(ellipse 30% 40% at 18% 35%, rgba(140,50,70,0.55) 0%, transparent 100%),
      radial-gradient(ellipse 30% 40% at 82% 35%, rgba(140,50,70,0.55) 0%, transparent 100%),
      linear-gradient(180deg, #2a1a4a 0%, #332a72 45%, #1f3cae 80%, var(--royal) 100%);
  }
  .logo-tab {
    position: absolute;
    left: 150px;
    top: 0;
    width: 256px;
    height: 92px;
    background: var(--tab-grey);
    border-radius: 0 0 38px 38px;
    display: flex;
    align-items: center;
    justify-content: center;
    gap: 10px;
  }
  .logo-tab .logo-dot {
    width: 22px; height: 22px;
    border-radius: 50%;
    background: var(--royal);
    flex: none;
  }
  .logo-tab .logo-name {
    font-weight: 700;
    font-size: 12.5px;
    line-height: 1.2;
    color: var(--royal);
    text-transform: uppercase;
    letter-spacing: 0.3px;
    width: 150px;
  }
  .headline {
    position: absolute;
    left: 0; right: 0;
    top: 236px;
    margin: 0;
    text-align: center;
    color: var(--white);
    font-family: "Poppins", sans-serif;
    font-weight: 900;
    line-height: 0.92;
    text-shadow: 4px 4px 0 var(--navy);
    letter-spacing: -2px;
  }
  .headline .line-were { display: block; font-size: 100px; padding-left: 40px; }
  .headline .line-hiring { display: block; font-size: 108px; }
  .role-bar {
    position: absolute;
    left: 0;
    right: 0;
    top: 476px;
    height: 70px;
  }
  .role-bar .rule {
    position: absolute;
    height: 2px;
    background: var(--ink);
  }
  .role-bar .rule-top { top: 0; left: 110px; right: 40px; }
  .role-bar .rule-bottom { bottom: 0; left: 60px; right: 90px; }
  .role-bar .role-row {
    position: absolute;
    left: 0; right: 0;
    top: 0; bottom: 0;
    display: flex;
    align-items: center;
    justify-content: center;
    gap: 16px;
  }
  .role-bar .tick-box { width: 42px; height: 36px; flex: none; }
  .role-bar .role-title {
    color: var(--white);
    font-family: "Poppins", sans-serif;
    font-weight: 900;
    font-size: 42px;
    letter-spacing: -1px;
    text-shadow: 3px 3px 0 var(--navy);
  }
  .intro {
    position: absolute;
    left: 150px;
    right: 30px;
    top: 560px;
    margin: 0;
    color: var(--white);
    font-weight: 300;
    font-size: 20px;
    line-height: 1.25;
    text-align: center;
  }
  .bottom-art { position: absolute; left: 0; top: 0; width: 556px; height: 860px; }
  .apply-pill {
    position: absolute;
    left: 120px;
    top: 672px;
    width: 340px;
    height: 46px;
    border-radius: 23px;
    background: var(--navy);
    border: 3px solid var(--royal-deep);
    display: flex;
    align-items: center;
    justify-content: center;
    gap: 6px;
    color: var(--white);
    font-size: 14px;
  }
  .apply-pill .apply-label { font-weight: 300; }
  .apply-pill .apply-email { font-weight: 800; font-size: 15px; }
  .web-address {
    position: absolute;
    left: 0; right: 0;
    bottom: 22px;
    text-align: center;
    color: var(--white);
    font-weight: 700;
    font-size: 11px;
    letter-spacing: 3px;
  }
</style>
</head>
<body>
  <main class="poster">
    <div class="theater-photo" role="img" aria-label="Photo of a historic downtown theater interior with ornate stage arch, lit in purple and red"></div>

    <div class="logo-tab">
      <span class="logo-dot"></span>
      <span class="logo-name">Brightline Stagecraft Company</span>
    </div>

    <h1 class="headline">
      <span class="line-were">We’re</span>
      <span class="line-hiring">HIRING</span>
    </h1>

    <svg class="bottom-art" viewBox="0 0 556 860">
      <defs>
        <linearGradient id="skylineTone" x1="0" y1="0" x2="0" y2="1">
          <stop offset="0" stop-color="#1e2a9a"/>
          <stop offset="0.55" stop-color="#3a3aa8"/>
          <stop offset="1" stop-color="#2a2478"/>
        </linearGradient>
        <linearGradient id="consoleTone" x1="0" y1="0" x2="1" y2="1">
          <stop offset="0" stop-color="#5a7fb8"/>
          <stop offset="0.45" stop-color="#2c3342"/>
          <stop offset="1" stop-color="#4a2230"/>
        </linearGradient>
        <linearGradient id="stageTone" x1="0" y1="0" x2="1" y2="1">
          <stop offset="0" stop-color="#8a2a8a"/>
          <stop offset="0.4" stop-color="#2b2a3e"/>
          <stop offset="1" stop-color="#55585f"/>
        </linearGradient>
      </defs>
      <polygon points="0,705 0,860 556,860 556,770 470,725 100,725" fill="url(#skylineTone)" stroke="#0a2a9a" stroke-width="4"
        role="img" aria-label="Photo of the downtown Los Angeles skyline at night"/>
      <polygon points="0,575 75,560 135,640 110,715 0,728" fill="url(#consoleTone)" stroke="#0630a0" stroke-width="4"
        role="img" aria-label="Photo of a digital audio mixing console"/>
      <polygon points="556,735 556,860 430,860 400,790 470,742" fill="url(#stageTone)" stroke="#0630a0" stroke-width="4"
        role="img" aria-label="Photo of a concert stage with colorful lighting rig"/>
    </svg>

    <div class="role-bar">
      <span class="rule rule-top"></span>
      <span class="rule rule-bottom"></span>
      <div class="role-row">
        <svg class="tick-box" viewBox="0 0 42 36" aria-hidden="true">
          <rect x="5" y="5" width="34" height="28" rx="3" fill="none" stroke="#07145a" stroke-width="4"/>
          <rect x="3" y="3" width="34" height="28" rx="3" fill="none" stroke="#ffffff" stroke-width="4"/>
          <path d="M11 17 L18 23 L30 10" fill="none" stroke="#ffffff" stroke-width="4" stroke-linecap="round" stroke-linejoin="round"/>
        </svg>
        <span class="role-title">TECHNICIANS</span>
      </div>
    </div>

    <p class="intro">We are looking for talented technicians to add to our roster of skilled professionals.</p>

    <div class="apply-pill">
      <span class="apply-label">send resume to:</span>
      <span class="apply-email">apply@bsccrewhub.la</span>
    </div>

    <div class="web-address">WWW.BSCCREWHUB.LA</div>
  </main>
</body>
</html>
```